Larchmont Vale Rehab and Wellness Postcard

This is a postcard for our chiropractic office, to raise awareness of our practice. Please refer to our grand opening flyer for contact information and logo. Please include the following:
Larchmont Vale Rehab and Wellness
Chiropractic & Wellness
Spinal Correction
Injury Rehabilitation
Tired of living with Fatigue, Allergies, High/Low Blood Pressure, Headaches, Numbness/Tingling in Hands/Feet, Frequent Infection, Back Pain, Neck Pain or ANY Other Health Problems?
Call Today for a Free Consultation with the Doctor!
(Space is Limited, Please Call to Reserve)

```html
<!DOCTYPE html>
<html lang="en">
<head>
<meta charset="utf-8">
<title>Larchmont Vale Rehab and Wellness Postcard</title>
<link href="https://fonts.googleapis.com/css2?family=Montserrat:wght@700;800&family=Roboto:wght@400;500;700&family=Open+Sans:wght@400;700&display=swap" rel="stylesheet">
<style>
  :root{
    --stage:#737373;
    --navy:#0d3457;
    --sky:#7aa3c8;
    --panel:#dcdcdc;
    --brand:#3a7bc0;
    --ink:#111;
    --white:#fff;
    --stamp:#ececec;
  }
  *{margin:0;padding:0;box-sizing:border-box}
  html,body{width:1200px;height:1200px;overflow:hidden;background:var(--stage)}
  .card{position:absolute;width:730px;height:497px;background:var(--white);overflow:hidden}
  .card--front{left:113px;top:94px}
  .card--back{left:337px;top:640px}
  .card svg.shapes{position:absolute;left:0;top:0}
  .abs{position:absolute}
  .brand{position:absolute;display:flex;flex-direction:column;align-items:center;text-align:center;
    font-family:"Roboto",sans-serif;font-weight:500;color:var(--brand);font-size:19px;line-height:1.15;letter-spacing:.5px}
  .brand__dot{width:40px;height:40px;border:3px solid var(--brand);border-radius:50%;margin-bottom:8px}
  .title{position:absolute;left:300px;width:430px;text-align:center;font-family:"Montserrat",sans-serif;font-weight:800;color:var(--navy);white-space:nowrap}
  .title--main{top:150px;font-size:32px}
  .title--sub{top:193px;font-size:27px}
  .services-list{position:absolute;left:414px;top:234px;list-style:none;font-family:"Roboto",sans-serif;font-weight:700;font-size:20px;color:var(--ink)}
  .services-list li{display:flex;align-items:center;height:29.5px}
  .bullet{width:14px;height:14px;border:2px solid var(--sky);border-radius:50%;margin-right:12px;flex:none}
  .pill{position:absolute;left:346px;top:339px;width:357px;height:38px;background:var(--navy);border-radius:19px;
    color:var(--white);text-align:center;font-family:"Montserrat",sans-serif}
  .pill__lead{font-weight:700;font-size:12.5px;padding-top:5px}
  .pill__note{font-family:"Open Sans",sans-serif;font-size:10px;margin-top:1px}
  .phone{font-family:"Montserrat",sans-serif;font-weight:800;color:var(--ink);white-space:nowrap}
  .small{font-family:Arial,Helvetica,sans-serif;font-size:12.5px;color:var(--ink);line-height:16px;white-space:nowrap}
  .small--white{color:var(--white)}
  .problems{position:absolute;list-style:none;font-family:"Open Sans",sans-serif;font-weight:700;font-size:11.5px;color:var(--ink);line-height:16px}
  .problems li{position:absolute;white-space:nowrap;padding-left:11px}
  .problems li::before{content:"";position:absolute;left:0;top:4px;width:8px;height:8px;border:1.5px solid var(--sky);border-radius:50%}
  .problems li.cont::before{display:none}
  .heading-services{position:absolute;left:29px;top:132px;font-family:"Open Sans",sans-serif;font-weight:700;font-size:28px;color:var(--white)}
  .cta-lead{font-family:"Montserrat",sans-serif;font-weight:700;font-size:12.5px;color:var(--navy)}
  .cta-note{font-family:"Open Sans",sans-serif;font-size:10.5px;color:var(--ink)}
  .stamp{position:absolute;left:640px;top:28px;width:61px;height:64px;background:var(--stamp)}
  .address-line{position:absolute;left:524px;width:177px;height:0;border-top:1.5px solid var(--ink)}
</style>
</head>
<body>

<!-- Front -->
<section class="card card--front">
  <svg class="shapes" width="730" height="497" viewBox="0 0 730 497">
    <rect x="0" y="0" width="730" height="18" fill="var(--navy)"/>
    <rect x="300" y="330" width="430" height="116" fill="var(--panel)"/>
    <rect x="0" y="446" width="730" height="51" fill="var(--sky)"/>
    <path d="M0,18 L176,18 Q492,322 250,497 L0,497Z" fill="var(--navy)"/>
    <path d="M0,18 L160,18 Q470,322 232,497 L0,497Z" fill="var(--sky)"/>
    <path d="M0,18 L146,18 Q450,322 216,497 L0,497Z" fill="#d9e4ea" role="img" aria-label="Photo: physiotherapist guiding a smiling woman through a resistance band shoulder exercise"/>
    <rect x="0" y="18" width="120" height="479" fill="#8d97a3" opacity=".35"/>
    <g fill="none" stroke="var(--ink)" stroke-width="1.6">
      <circle cx="434" cy="394" r="7.5"/>
      <path d="M430.5,390.5 q0,6 6.5,7.5 l1.2,-1.6 -2,-1.4 -1,1 q-2.4,-1 -3,-3.2 l1,-1 -1.2,-2 z" fill="var(--ink)" stroke="none"/>
    </g>
    <path d="M433,421 c-3.5,0 -5.5,2.6 -5.5,5.2 c0,3.6 5.5,9.6 5.5,9.6 s5.5,-6 5.5,-9.6 c0,-2.6 -2,-5.2 -5.5,-5.2z" fill="var(--navy)"/>
    <circle cx="433" cy="426.5" r="2" fill="var(--panel)"/>
    <g fill="none" stroke="var(--navy)" stroke-width="1.2">
      <rect x="338" y="458" width="12" height="8"/>
      <path d="M338,458 l6,5 6,-5"/>
      <circle cx="544" cy="462" r="5.5"/>
      <ellipse cx="544" cy="462" rx="2.3" ry="5.5"/>
      <path d="M538.5,462 h11"/>
    </g>
  </svg>

  <div class="brand" style="left:435px;top:34px;width:200px">
    <span class="brand__dot"></span>
    <span>Larchmont Vale</span>
    <span>Rehab</span>
  </div>

  <h1 class="title title--main">LARCHMONT VALE</h1>
  <h2 class="title title--sub">REHAB AND WELLNESS</h2>

  <ul class="services-list">
    <li><span class="bullet"></span>Chiropractic &amp; Wellness</li>
    <li><span class="bullet"></span>Spinal Correction</li>
    <li><span class="bullet"></span>Injury Rehabilitation</li>
  </ul>

  <div class="pill">
    <p class="pill__lead">Call Today for a Free Consultation with the Doctor!</p>
    <p class="pill__note">(Space is Limited, Please Call to Reserve)</p>
  </div>

  <p class="phone abs" style="left:454px;top:378px;font-size:24px">555-014-2290</p>
  <p class="small abs" style="left:454px;top:412px">Larchmont Vale Rehab 410 Orchard Avenue,<br>Suite 220 Larchmont Vale, NJ 07990</p>
  <p class="small small--white abs" style="left:359px;top:454px">info@larchmontvale.com</p>
  <p class="small small--white abs" style="left:558px;top:454px">www.larchmontvale.com</p>
</section>

<!-- Back -->
<section class="card card--back">
  <svg class="shapes" width="730" height="497" viewBox="0 0 730 497">
    <defs>
      <clipPath id="leftPanel"><path d="M0,0 L319,0 Q543,248 319,497 L0,497Z"/></clipPath>
      <clipPath id="roundPhoto"><circle cx="423" cy="260" r="52"/></clipPath>
    </defs>
    <g clip-path="url(#leftPanel)">
      <rect x="0" y="0" width="730" height="133" fill="#d8b9a4" role="img" aria-label="Photo: practitioner's hands on a patient's upper back with the spine highlighted"/>
      <rect x="0" y="0" width="110" height="133" fill="#eef1f3"/>
      <rect x="0" y="133" width="730" height="41" fill="var(--sky)"/>
      <rect x="0" y="320" width="730" height="122" fill="var(--panel)"/>
      <rect x="0" y="442" width="730" height="55" fill="var(--sky)"/>
    </g>
    <path d="M319,-4 Q551,248 319,501" fill="none" stroke="var(--navy)" stroke-width="15"/>
    <circle cx="423" cy="260" r="56" fill="var(--white)" stroke="var(--sky)" stroke-width="4"/>
    <g clip-path="url(#roundPhoto)">
      <rect x="371" y="208" width="104" height="104" fill="#e6d3c4" role="img" aria-label="Photo: man relaxing during a back massage"/>
    </g>
    <g fill="none" stroke="var(--navy)" stroke-width="1.6">
      <circle cx="38" cy="372" r="7.5"/>
    </g>
    <path d="M34.5,368.5 q0,6 6.5,7.5 l1.2,-1.6 -2,-1.4 -1,1 q-2.4,-1 -3,-3.2 l1,-1 -1.2,-2 z" fill="var(--navy)"/>
    <g fill="none" stroke="var(--navy)" stroke-width="1.2">
      <rect x="30" y="390" width="12" height="8"/>
      <path d="M30,390 l6,5 6,-5"/>
      <circle cx="93" cy="460" r="5.5"/>
      <ellipse cx="93" cy="460" rx="2.3" ry="5.5"/>
      <path d="M87.5,460 h11"/>
    </g>
    <path d="M34,409 c-3.5,0 -5.5,2.6 -5.5,5.2 c0,3.6 5.5,9.6 5.5,9.6 s5.5,-6 5.5,-9.6 c0,-2.6 -2,-5.2 -5.5,-5.2z" fill="var(--navy)"/>
    <circle cx="34" cy="414.5" r="2" fill="var(--panel)"/>
  </svg>

  <h2 class="heading-services">services</h2>

  <ul class="problems" style="left:33px;top:182px">
    <li style="top:0">Tired of living with</li>
    <li style="top:16px">Fatigue,</li>
    <li style="top:35px">Allergies,</li>
    <li style="top:54px">High/Low Blood Pressure,</li>
    <li style="top:73px">Headaches,</li>
    <li style="top:93px">Numbness/Tingling in</li>
    <li class="cont" style="top:109px">Hands/Feet,</li>
  </ul>
  <ul class="problems" style="left:210px;top:182px">
    <li style="top:0">Frequent Infection,</li>
    <li style="top:19px">Back Pain,</li>
    <li style="top:38px">Neck Pain or ANY Other</li>
    <li class="cont" style="top:54px">Health Problems?</li>
  </ul>

  <p class="cta-lead abs" style="left:30px;top:326px">Call Today for a Free Consultation with the Doctor!</p>
  <p class="cta-note abs" style="left:30px;top:343px">(Space is Limited, Please Call to Reserve)</p>
  <p class="phone abs" style="left:57px;top:360px;font-size:20px">555-014-2290</p>
  <p class="small abs" style="left:50px;top:386px">info@larchmontvale.com</p>
  <p class="small abs" style="left:49px;top:406px">Larchmont Vale Rehab 410 Orchard Avenue,<br>Suite 220 Larchmont Vale, NJ 07990</p>
  <p class="small small--white abs" style="left:104px;top:452px">www.larchmontvale.com</p>

  <div class="brand" style="left:387px;top:26px;width:200px;font-size:17px">
    <span class="brand__dot" style="width:34px;height:34px;margin-bottom:6px"></span>
    <span>Larchmont Vale</span>
    <span>Rehab</span>
  </div>

  <div class="stamp"></div>
  <div class="address-line" style="top:229px"></div>
  <div class="address-line" style="top:258px"></div>
  <div class="address-line" style="top:287px"></div>
</section>

</body>
</html>
```